Flyer-Design für Keramik Verdunster
Zielgruppe
Wir wollen Keramik Verdunster bei Volkarn Verkaufen und dieser Flyer soll in jede Produktverpackung mit hinein gelegt werden.
Aufgabenstellung
Der Flyer sollte möglichst klein gehalten werden, also mehrmals Faltbar. Kann auf Vorder- und Rückseite bedruckt werden.
Ihrer Kreativität sind von unserer seite aus ,keine Grenzen gesetzt.
Im Anhang unser Logo , was mit auf den Flyer muss und in der Worddatei haben wir in Klammern noch Instruktionen für sie mit reingeschrieben. Design ect. ist Ihnen überlassen

```html
<!DOCTYPE html>
<html lang="de">
<head>
<meta charset="utf-8">
<title>Norvessa Faltflyer – Anleitung für ein ideales Raumklima</title>
<link href="https://fonts.googleapis.com/css2?family=Lato:wght@400;700&display=swap" rel="stylesheet">
<style>
:root{
  --blue:#0a84c8;
  --blue-box:rgba(10,132,200,.88);
  --blue-soft:#4a9bd6;
  --heading:#1a8ad0;
  --ink:#1d1d1d;
  --navy:#1c2560;
  --panel-tint:#e6edf8;
  --table-row:#e4f1fb;
  --table-head:#cfe6f7;
  --fold:#5e5e5e;
  --white:#ffffff;
}
*{margin:0;padding:0;box-sizing:border-box}
html,body{width:1200px;height:611px;overflow:hidden;background:#fff}
body{font-family:'Lato',sans-serif;color:var(--ink);font-size:8px;line-height:10.2px;position:relative}
.sheet{position:absolute;inset:0}
.row{position:absolute;left:0;width:1200px;height:300px}
.row--outer{top:0}
.row--inner{top:311px}
.fold-band{position:absolute;left:0;top:300px;width:1200px;height:11px;background:var(--fold)}
.panel{position:absolute;top:0;height:300px;width:300px;overflow:hidden}
.p1{left:0}.p2{left:300px}.p3{left:600px}.p4{left:900px}
.photo{position:absolute;inset:0}
.photo--radiator{background:linear-gradient(120deg,#eef0f1 0%,#dcdfe2 45%,#f3f4f5 100%)}
.photo--sky{background:linear-gradient(170deg,#2f72c4 0%,#6aa2dc 45%,#c9dcef 75%,#8fb5df 100%)}
.photo--rest{left:300px;width:600px;height:300px;background:linear-gradient(100deg,#eef1ec 0%,#c9d7b2 30%,#f1f2ee 55%,#dfe6dc 75%,#c9d3d8 100%)}
.info-box{position:absolute;color:var(--white);background:var(--blue-box);padding:8px 12px}
.info-box p+p{margin-top:10px}
.box-drying{left:0;top:216px;width:249px;height:71px;padding:8px 17px;background:var(--blue)}
.panel--tint{background:var(--panel-tint)}
h2{color:var(--heading);font-weight:700;font-size:9.6px;line-height:11.5px}
.steps{position:absolute;left:19px;top:24px;width:265px}
.steps ol{list-style:none;margin-top:19px}
.steps li+li{margin-top:10px}
.card{position:absolute;background:rgba(255,255,255,.88)}
.card--airing{left:9px;top:15px;width:181px;height:270px;padding:7px 7px}
.card--airing h2{margin-bottom:8px}
.card--airing p+p{margin-top:10px}
.card--duration{left:196px;top:97px;width:104px;height:159px;padding:8px 6px}
.card--duration h3{font-size:8px;font-weight:700;margin-bottom:11px}
.duration td{padding:0;line-height:10.2px}
.duration td:first-child{width:54px}
.brand{text-align:center;padding-top:125px}
.brand__mark{width:46px;height:46px;border-radius:50%;background:var(--navy);margin:0 auto 16px}
.brand__name{font-size:17px;letter-spacing:6px;color:var(--navy);font-weight:400}
.brand__claim{font-size:11.5px;font-weight:700;margin-top:16px;color:var(--ink)}
.guide{position:absolute;left:15px;top:23px;width:276px}
.guide .lead{margin-top:7px}
.guide h4{font-size:8px;font-weight:700;margin-top:19px}
.guide .intro{margin-top:11px}
.guide h5{color:var(--heading);font-size:8.3px;font-weight:700;margin-top:11px}
.climate{position:absolute;left:15px;top:177px;width:273px;border-collapse:collapse}
.climate th,.climate td{text-align:left;padding:0 4px;height:15.3px;font-size:8px}
.climate th{background:var(--table-head);font-weight:700}
.climate tr:nth-child(odd) td{background:var(--table-row)}
.box-kitchen{left:342px;top:169px;width:258px;height:107px;padding:9px 8px}
.box-facts{left:625px;top:109px;width:258px;height:164px;padding:12px 13px}
.box-facts h3{font-size:8px;font-weight:700;margin-bottom:10px}
.panel--review{background:var(--blue);color:var(--white);text-align:center}
.stars{margin-top:102px;display:flex;justify-content:center;gap:3px}
.review{font-size:10.5px;line-height:12.6px;font-weight:700;text-transform:uppercase;margin-top:20px}
.review+.review{margin-top:13px}
</style>
</head>
<body>
<div class="sheet">

  <section class="row row--outer">
    <div class="panel p1">
      <div class="photo photo--radiator" role="img" aria-label="Foto: weißer Heizkörper unter einem Fenster mit Zimmerpflanze"></div>
      <div class="info-box box-drying"><p>Die Verdunstungsdauer hängt von den verschiedensten Faktoren ab. Je gesättigter Ihre relative Luftfeuchtigkeit im Raum (durch schlechtes Lüften) und je kälter der Heizkörper desto Länger dauert der Verdunstungsprozess! Die Luft kann dadurch nicht mehr Feuchtigkeit aufnehmen!</p></div>
    </div>

    <div class="panel p2 panel--tint">
      <div class="steps">
        <h2>Was muss ich beachten und wie funktionieren meine neuen Norvessa Heizkörper Luftbefeuchter.</h2>
        <ol>
          <li>1. Füllen Sie Ihre neuen Luftbefeuchter mit warmen Wasser, idealerweise mit entkalktem Wasser.</li>
          <li>2. Sollten Sie kein entkalktes Wasser haben , sollten Sie Ihre Verdunster nach jedem Durchgang (Komplett Verdunstet) mit verdünntem Essig oder Zitronensäure von innen reinigen, um die Poren Kalkfrei zu halten und um eine optimale Verdunstung zu gewährleisten.</li>
          <li>3. Um weiterhin eine optimale Verdunstung zu gewährleisten, sollte Ihr Heizkörper so warm sein, dass Sie ihn gerade noch mit der Hand anfassen können oder noch heißer.</li>
          <li>4. Bringen Sie an jedem Heizkörper zwei Verdunster an. Außer im Bad und der Küche!</li>
          <li>5. Wenn die Verdunster zu lange an einem Heizkörper hängen, die abgeschaltet bzw. kalt sind ,dann kann es zur Tröpfchenbildung kommen, weil die Poren groß sind und bei kalter Oberfläche kann das Wasser nicht schnell genug verdunsten.</li>
        </ol>
      </div>
    </div>

    <div class="panel p3">
      <div class="photo photo--sky" role="img" aria-label="Foto: blauer Himmel mit Wolken und fliegender Möwe"></div>
      <div class="card card--airing">
        <h2>Richtiges Lüften</h2>
        <p>Schließen Sie den Thermostatkopf der Heizungen komplett. Öffnen Sie die Fenster zweier gegenüberliegender Räume gleichzeitig und lassen auch die Türen offen stehen.</p>
        <p>Auf diese Weise entsteht ein Durchzug und die warme, verbrauchte Luft zieht schneller nach draußen ab.</p>
        <p>Achtung: Vergessen Sie nicht, auch im zweiten Raum, den Heizkörper während des Lüftens abzustellen!</p>
        <p>Wie oft sollten Sie Lüften? Optimal wäre 4 mal am Tag, da dies aber oft nicht möglich ist, sollten Sie mindestens 2 mal am Tag Lüften, Abends vor dem Schlafen gehen und Morgens nach dem Aufstehen.</p>
        <p>Wenn Sie nun so vorgehen wie beschrieben, wird Ihnen und dem wunderbaren Gefühl eines schönen Klimas im Zuhause, nichts mehr im Wege stehen.</p>
      </div>
      <div class="card card--duration">
        <h3>Dauer des Lüftens:</h3>
        <table class="duration">
          <tr><td>Januar</td><td>5 min</td></tr>
          <tr><td>Februar</td><td>5 min</td></tr>
          <tr><td>März</td><td>10 min</td></tr>
          <tr><td>April</td><td>15 min</td></tr>
          <tr><td>Mai</td><td>20 min</td></tr>
          <tr><td>Juni</td><td>30 min</td></tr>
          <tr><td>Juli</td><td>30 min</td></tr>
          <tr><td>August</td><td>30 min</td></tr>
          <tr><td>September</td><td>15 min</td></tr>
          <tr><td>Obtober</td><td>20 min</td></tr>
          <tr><td>November</td><td>10 min</td></tr>
          <tr><td>Dezember</td><td>5 min</td></tr>
        </table>
      </div>
    </div>

    <div class="panel p4 brand">
      <div class="brand__mark"></div>
      <div class="brand__name">NORVESSA</div>
      <div class="brand__claim">Anleitung für ein ideales Raumklima</div>
    </div>
  </section>

  <div class="fold-band"></div>

  <section class="row row--inner">
    <div class="panel p1">
      <div class="guide">
        <h2>Anleitung für ein Ideales Raumklima und die optimale Luftfeuchtigkeit mit Ihrem Norvessa Heizkörper Luftbefeuchter!</h2>
        <p class="lead">Für ein schönes Klima sorgen Sie, wie Folgt:</p>
        <h4>relative Luftfeuchtigkeit in Wohnräumen</h4>
        <p class="intro">In der folgenden Tabelle finden Sie die optimalen Werte für relative Luftfeuchte und Temperatur in den verschiedenen Wohnbereichen.<br>Als ideale Mittelwerte haben sich 40 - 60 % Feuchte und 20 °C Raumtemperatur bewährt.</p>
        <h5>Ideales Raumklima</h5>
      </div>
      <table class="climate">
        <tr><th>Raum</th><th>Optimale Temperatur</th><th>Optimale Luftfeuchtigkeit</th></tr>
        <tr><td>Wohnräume</td><td>20 °C</td><td>40 - 60 %</td></tr>
        <tr><td>Schlafzimmer</td><td>16 - 18 °C</td><td>40 - 60 %</td></tr>
        <tr><td>Kinderzimmer</td><td>20 - 22 °C</td><td>40 - 60 %</td></tr>
        <tr><td>Küche</td><td>18 °C</td><td>50 - 60 %</td></tr>
        <tr><td>Badezimmer</td><td>23 °C</td><td>50 - 70 %</td></tr>
        <tr><td>Keller</td><td>10 - 15 °C</td><td>50 - 65 %</td></tr>
      </table>
    </div>

    <div class="photo photo--rest" role="img" aria-label="Foto: entspannte Person ruht auf einem Sofa in einem hellen Raum mit Grünpflanzen"></div>

    <div class="info-box box-kitchen">
      <p>Naturgemäß liegt die Luftfeuchte in Küche und Bad etwas höher und kann beim Kochen oder Duschen auch über diese Werte steigen.</p>
      <p>Das ist kein Problem, solange der Zustand nicht dauerhaft anhält. Dennoch sollte es Ihnen zur Gewohnheit werden, sofort nach dem Kochen oder Duschen den Wasserdampf nach draußen entweichen zu lassen.</p>
    </div>

    <div class="info-box box-facts" style="background:rgba(74,155,214,.92)">
      <h3>Wissenswertes zur Luftfeuchtigkeit</h3>
      <p>Das gesündeste Raumklima herrscht bei 50 % relativer Luftfeuchte und 20 °C Raumtemperatur.</p>
      <p>Die relative Raumfeuchte sollte nicht unter 30 % fallen.</p>
      <p>Einige Schimmelpilzarten vermehren sich bereits ab 70 % Feuchtigkeit.</p>
      <p>Herrschen über einen längeren Zeitraum mehr als 80 % Feuchtigkeit im Raum, führt das unvermeidlich zur Entstehung von Schimmel.</p>
    </div>

    <div class="panel p4 panel--review">
      <div class="stars" aria-label="Fünf Sterne">
        <svg width="72" height="13" viewBox="0 0 72 13">
          <g fill="#fff">
            <polygon id="star" points="6.5,0 8.1,4.6 13,4.7 9.1,7.7 10.5,12.4 6.5,9.6 2.5,12.4 3.9,7.7 0,4.7 4.9,4.6"/>
            <use href="#star" x="14.7"/><use href="#star" x="29.4"/><use href="#star" x="44.1"/><use href="#star" x="58.8"/>
          </g>
        </svg>
      </div>
      <p class="review">Sie sind zufrieden mit unserem Produkt<br>und dieser Anleitung?</p>
      <p class="review">Dann hinterlassen Sie uns doch bitte<br>eine Rezension auf Volkarn.</p>
    </div>
  </section>

</div>
</body>
</html>
```